Vaultrix Web Site

Hi Designers. Our web site at www.vaultrix.net.au needs a new look.

We do:

- off-site backup, every day, for vital data
- data recovery from crashed disks

We have an existing logo

Our colour is blue. Our image is about Trust and Competence

We are in Perth, Western Australia. Our photographs are local images.

We've been in business for fifteen years.

We have a second URL too: www.keep-our-records.com.au

Both URLs go to the same web site.

Would you like to take on this project?

Target Market(s)

Target market is small to medium business, with between 5 and 100 staff. Customers are mainly in Australia but can be anywhere. There are other providers who are cheaper- our point of difference is that we are highly professional and have been in the business for 15 years. personal attention is important to us- we promise Extreme Service.

Industry/Entity Type

Data Recovery

Requirements
Must have
• Our image is about Trust and Competence. Existing text from our web site can be used.
Should not have
• No moving Flash, no Flash intro

```html
<!DOCTYPE html>
<html lang="en">
<head>
<meta charset="utf-8">
<title>Keep Our Records – Vaultrix Computer Services</title>
<link rel="stylesheet" href="https://fonts.googleapis.com/css2?family=Arimo:wght@400;700&display=swap">
<style>
  :root {
    --navy: #0b416c;
    --navy-text: #0e3f6b;
    --page-bg: #c3d1dd;
    --tab: #c8d4df;
    --white: #ffffff;
    --panel: rgba(236, 241, 246, 0.92);
    --stripe: #6b8eab;
    --server-dark: #6f8aa2;
    --server-light: #c4d2de;
  }
  * { box-sizing: border-box; margin: 0; padding: 0; }
  html, body { width: 1200px; height: 996px; overflow: hidden; }
  body {
    position: relative;
    background: var(--page-bg);
    font-family: "Arimo", Arial, sans-serif;
    color: var(--navy-text);
  }
  .header-top {
    position: absolute; left: 0; top: 0; width: 1200px; height: 193px;
    background: var(--white);
  }
  .brand-band {
    position: absolute; left: 0; top: 193px; width: 1200px; height: 113px;
    background: var(--navy);
    box-shadow: 0 3px 4px rgba(0,0,0,0.25);
  }
  .brand-mark {
    position: absolute; left: 132px; top: 58px; width: 96px; height: 96px;
    border-radius: 50%; background: var(--navy);
  }
  .brand-name {
    position: absolute; left: 309px; top: 80px;
    font-size: 52px; font-weight: 700; color: var(--navy);
    letter-spacing: 0.5px; white-space: nowrap;
  }
  .main-nav {
    position: absolute; left: 119px; top: 174px; width: 969px; height: 49px;
    background: var(--navy);
  }
  .main-nav a {
    position: absolute; top: 15px; width: 150px; height: 19px;
    background: var(--tab); color: var(--navy-text);
    font-size: 13px; font-weight: 700; text-align: center; line-height: 19px;
    text-decoration: none;
  }
  .main-nav a.is-current { background: var(--white); }
  .main-nav a.is-current::after {
    content: ""; position: absolute; left: 68px; top: 19px;
    border-left: 7px solid transparent; border-right: 7px solid transparent;
    border-top: 7px solid var(--white);
  }
  .hero {
    position: absolute; left: 119px; top: 223px; width: 969px; height: 296px;
    box-shadow: 2px 3px 4px rgba(0,0,0,0.35);
  }
  .hero-photo {
    position: absolute; inset: 0;
    background: linear-gradient(90deg, #2f3333 0%, #5a5853 30%, #9a7a5c 45%, #e7ecef 70%, #f1f3f4 100%);
  }
  .hero-panel {
    position: absolute; left: 739px; top: 7px; width: 222px; height: 282px;
    background: var(--panel); padding: 14px 15px;
    font-weight: 700; color: var(--navy-text);
  }
  .hero-panel h2 { font-size: 19px; line-height: 32px; }
  .hero-panel p { font-size: 15px; line-height: 32px; margin-top: 33px; }
  .feature {
    position: absolute; left: 119px; top: 527px; width: 719px; height: 371px;
    background: var(--stripe);
  }
  .feature-photo {
    position: absolute; left: 0; top: 0; width: 719px; height: 335px;
    background: linear-gradient(90deg, var(--server-light) 0%, #9fb3c5 25%, var(--server-dark) 60%, #7e97ad 100%);
  }
  .feature-fold {
    position: absolute; right: 0; top: 0; width: 32px; height: 32px;
    background: linear-gradient(225deg, var(--page-bg) 50%, #4d7192 50%);
  }
  .feature h1 {
    position: absolute; left: 19px; top: 10px;
    font-size: 39px; font-weight: 700; color: var(--navy-text);
  }
  .feature-list {
    position: absolute; left: 91px; top: 68px; list-style: none;
    font-size: 15.5px; line-height: 32.3px; color: var(--navy-text);
  }
  .testimonials {
    position: absolute; left: 849px; top: 527px; width: 239px; height: 371px;
    background: var(--white); overflow: hidden;
    box-shadow: 2px 3px 4px rgba(0,0,0,0.35);
    padding: 14px 24px 0 24px;
    color: var(--navy-text);
  }
  .testimonials h2 {
    font-size: 24px; font-weight: 700; text-align: center;
    border-bottom: 2px solid var(--navy-text); padding-bottom: 1px;
    margin: 0 14px;
  }
  .testimonials h3 { font-size: 14px; font-weight: 700; line-height: 15px; margin-top: 32px; }
  .quote { font-size: 13px; line-height: 13px; margin-top: 32px; }
  .quote p { text-indent: 30px; }
  .quote cite { display: block; font-style: normal; text-indent: 30px; }
  .site-footer {
    position: absolute; left: 119px; top: 908px; width: 969px; height: 48px;
    background: var(--navy); color: var(--white);
    font-size: 13px; font-weight: 700; text-align: right;
    padding-right: 22px; line-height: 48px;
  }
</style>
</head>
<body>
  <div class="header-top"></div>
  <div class="brand-band"></div>

  <div class="brand-mark"></div>
  <div class="brand-name">Keep Our Records</div>

  <nav class="main-nav">
    <a class="is-current" href="#" style="left:9px">Home</a>
    <a href="#" style="left:169px">Remote Backup</a>
    <a href="#" style="left:330px">Emergency Recovery</a>
    <a href="#" style="left:490px">Testimonial</a>
    <a href="#" style="left:651px">Our Client</a>
    <a href="#" style="left:811px">About Us</a>
  </nav>

  <section class="hero">
    <div class="hero-photo" role="img" aria-label="Photo of a smiling office worker at her desk"></div>
    <div class="hero-panel">
      <h2>Vaultrix Computer Services</h2>
      <p>We keep your business records safe, always. Backup your critical data off-site, every night.</p>
    </div>
  </section>

  <section class="feature">
    <div class="feature-photo" role="img" aria-label="Photo of a row of servers in a data centre"></div>
    <div class="feature-fold"></div>
    <h1>Safe and Secure</h1>
    <ul class="feature-list">
      <li>Reliable backup is a vital part of risk management</li>
      <li>We keep your business records safe, always</li>
      <li>Database? Customer List? Financials? Contracts?</li>
      <li>Every hard disk fails one day</li>
      <li>We backup these valuable assets</li>
      <li>Critical data backup off-site, every night</li>
      <li>Located in Perth, Western Australia- the safest place on Earth</li>
      <li>Click HERE to find out more</li>
    </ul>
  </section>

  <aside class="testimonials">
    <h2>TESTIMONIALS</h2>
    <h3>What Clients think of our Service...</h3>
    <div class="quote">
      <p>“I've honestly never seen service like it.”</p>
      <cite>Martin Cole, Harbourline Capital</cite>
    </div>
    <div class="quote">
      <p>"Thank you for all your wonderful support - what would we do without you?"</p>
      <cite>Anna Price, Family Care Network of WA</cite>
    </div>
    <div class="quote">
      <p>"Greg you are a legend. We have an audit in progress today and I was able to illustrate a "Live" recovery. Thank you for</p>
    </div>
  </aside>

  <footer class="site-footer">©2011 - Vaultrix Computer Services</footer>
</body>
</html>
```